velvet moon parlor

My business is an adult toy and lingerie store. I need a catalogue listing multiple products on one page along with descriptions and prices. They must be two sided and in color. I can provide a sample to illustrate my request. I have hundreds of products . This is an actual hard copy catalogue I'm asking for.
I just uploaded a excel file . please tell if you are able to use/ open this file;.
Adults only
Adult

```html
<!DOCTYPE html>
<html lang="en">
<head>
<meta charset="utf-8">
<title>Velvet Moon Parlor — Catalogue Spread</title>
<link href="https://fonts.googleapis.com/css2?family=Crimson+Text:wght@400;600;700&display=swap" rel="stylesheet">
<style>
  :root {
    --backdrop: #d9d9d9;
    --paper: #ffffff;
    --ink: #1c1c1c;
    --rule: #cfcfcf;
    --latex-dark: #17171a;
    --wall-brown: #8a7560;
    --violet: #7b5fc2;
    --violet-deep: #55379a;
    --skin: #d9a98e;
    --hair: #6b3e26;
    --studio-grey: #dedfe0;
    --nude-latex: #d8c39a;
  }
  * { box-sizing: border-box; margin: 0; padding: 0; }
  html, body { width: 1200px; height: 1071px; overflow: hidden; }
  body {
    background: var(--backdrop);
    font-family: "Crimson Text", Georgia, serif;
    color: var(--ink);
    position: relative;
  }
  .spread {
    position: absolute; left: 40px; top: 135px;
    width: 1120px; height: 800px;
    display: flex;
    box-shadow: 0 6px 24px rgba(0,0,0,.18);
  }
  .page { position: relative; width: 560px; height: 800px; background: var(--paper); overflow: hidden; }
  .page--left { border-right: 1px solid var(--rule); }
  .photo { position: absolute; }
  .tag { position: absolute; font-size: 13px; color: var(--ink); z-index: 2; }
  .tag--light { color: #fff; }
  .item { position: absolute; font-size: 10.5px; line-height: 1.3; }
  .item--small { font-size: 8.5px; line-height: 1.3; }
  .item h3 { display: inline; font-weight: 700; font-size: 1.15em; }
  .item strong { font-weight: 700; }
  .item .sku { display: block; font-weight: 700; margin-top: 2px; }
  .brand-line { position: absolute; left: 24px; top: 10px; font-size: 17px; }

  .photo-latex { left: 0; top: 0; width: 232px; height: 500px;
    background: linear-gradient(180deg, #a89077 0%, var(--wall-brown) 45%, #4a3c30 100%); }
  .photo-collar { left: 0; top: 508px; width: 262px; height: 292px;
    background: linear-gradient(180deg, var(--hair) 0%, var(--skin) 45%, #3a2a22 100%); }
  .photo-vinyl-set { left: 272px; top: 485px; width: 150px; height: 290px;
    background: linear-gradient(160deg, var(--violet) 0%, var(--violet-deep) 100%); }
  .photo-laceup { left: 430px; top: 475px; width: 125px; height: 290px;
    background: linear-gradient(160deg, #8d74cf 0%, var(--violet-deep) 100%); }

  .photo-vest { left: 62px; top: 42px; width: 110px; height: 352px;
    background: linear-gradient(180deg, #f2f2f2 0%, #3a3a3a 20%, var(--latex-dark) 100%); }
  .photo-bodysuit { left: 362px; top: 150px; width: 180px; height: 290px;
    background: linear-gradient(180deg, var(--studio-grey) 0%, #8e8e90 50%, var(--studio-grey) 100%); }
  .photo-police { left: 40px; top: 410px; width: 140px; height: 300px;
    background: linear-gradient(180deg, #f4f4f4 0%, #2a2a2e 25%, var(--latex-dark) 100%); }
  .photo-briefs { left: 232px; top: 610px; width: 150px; height: 128px;
    background: linear-gradient(180deg, #f3f3f3 0%, #1e1e22 40%, #0e0e10 100%); }
  .photo-diaper { left: 398px; top: 610px; width: 150px; height: 128px;
    background: linear-gradient(180deg, #faf6ee 0%, var(--nude-latex) 60%, #b89f70 100%); }
</style>
</head>
<body>
<main class="spread">

  <section class="page page--left">
    <div class="photo photo-latex" role="img" aria-label="Model from behind in shoulder length latex gloves and latex thigh-high stockings"></div>
    <span class="tag" style="left:135px;top:62px">A</span>
    <span class="tag" style="left:150px;top:235px">B</span>

    <div class="item" style="left:244px;top:12px;width:170px">
      <h3>A. Shoulder Length Latex Gloves</h3> A stimulating accessory to your fetish wardrobe. Great for sexual play, caressing the body with latex is an experience! High quality gloves are imported from England. Comes in 3 sizes. The medium fits most.
      <span class="sku">DE110 - $45.00</span>
    </div>
    <div class="item" style="left:244px;top:150px;width:170px">
      <h3>B. Latex Thigh-high Stockings</h3> Sexy latex stockings to complete your fetish wardrobe. These Seamless latex stockings have small rolled edges at the tops. Premium quality, imported from London. <strong>Available in small, medium, &amp; large</strong>
      <span class="sku">DE106 - $90.00</span>
    </div>
    <div class="item" style="left:244px;top:285px;width:170px">
      <h3>C. Suede Leather Collar With O-ring</h3> This luxurious Ardent Hide Suede Collar sports a sturdy adjustable buckle strap, quality O ring pendant detail, and refined sewn soft leather piping. What a stunning fashion statement in and out of the bedroom. Comfort, quality and durability is what this collar is all about. <strong>Adjustable buckle</strong> 14" to 19" neck. Neck strap 1.5" wide. Front leather plunge 7" long.
      <span class="sku">AB843 - $57.50</span>
    </div>

    <div class="item item--small" style="left:426px;top:6px;width:128px">
      <h3>D. Vinyl Bustier With Zipper</h3> Women of all shapes and sizes will look and feel incredibly sexy in this flattering vinyl bustier, and your partner will undoubtedly agree. The smooth, shiny black front can be unzipped as much as you like to reveal a little or a lot. <strong>Available in small, medium, and large.</strong>
      <span class="sku">AB563 - $28.12</span>
    </div>
    <div class="item item--small" style="left:426px;top:165px;width:128px">
      <h3>E. Vinyl Lace Up Mini Shorts</h3> These shorts have an enticing lace up opening and sexy back lace up detailing. The low rise makes the torso look longer, while the high cut thigh elongates the legs, for an incredibly seductive silhouette. <strong>Size Small</strong> fits 26 inch waist, 28.5 inch low waist, 36 inch hips. See the sizing chart.
      <span class="sku">AB559-S - $12.75</span>
    </div>

    <div class="photo photo-collar" role="img" aria-label="Close portrait of a model wearing the suede leather collar with O-ring"></div>
    <span class="tag" style="left:190px;top:740px">C</span>
    <div class="photo photo-vinyl-set" role="img" aria-label="Model in black vinyl bustier and vinyl trousers against a purple wall"></div>
    <span class="tag tag--light" style="left:280px;top:495px">D</span>
    <div class="photo photo-laceup" role="img" aria-label="Model in vinyl lace up top and mini shorts against a purple wall"></div>
    <span class="tag tag--light" style="left:540px;top:485px">E</span>
  </section>

  <section class="page page--right">
    <div class="brand-line">Velvet Moon Parlor LLC ©</div>

    <span class="tag" style="left:20px;top:60px">A</span>
    <div class="photo photo-vest" role="img" aria-label="Male model in black leather vest and leather trousers"></div>

    <div class="item" style="left:182px;top:42px;width:165px">
      <h3>A. Mens Leather Vest</h3> Our men's black leather vest is a stylish high quality garment that will look great out on the town. Perfect for any leather lifestyler, the black leather vest is a look that never goes out of style. Add your club patch to personalize it. Also an excellent way to display your event pins. <strong>Available in M, L, &amp; X-L.</strong>
      <span class="sku">AT250 - $115.00</span>
    </div>
    <div class="item" style="left:358px;top:42px;width:150px">
      <h3>D. Latex Diaper</h3> A total must for all role plays! High-cut transparent diaper briefs with reinforced edges. Nothing will leak! Without inlay. <strong>Available in S,M,L,X-L</strong>
      <span class="sku">AA141 - $36.58</span>
    </div>
    <div class="item" style="left:182px;top:210px;width:168px">
      <h3>B. Police Leather Pants With Blue Stripe</h3> Hot Leather Uniform Pants. It does not get any more comfortable or sexier than our police leather pants. They are made from buttersoft lamb skin leather, that hug the hips and legs just right. These pants have a blue pin stripe going down each leg. Inseam is 33 inches and bottom of pants are not hemmed allowing you to have them adjusted in length if desired.
      <strong style="display:block;margin-top:4px">Available Sizes 30, 32, 34, 36, &amp; 38 Comes in Blue &amp; Red</strong>
      <span class="sku">AT147 - $126.35</span>
    </div>

    <div class="photo photo-bodysuit" role="img" aria-label="Two models in full black blackout body suits"></div>
    <span class="tag" style="left:385px;top:168px">E</span>

    <span class="tag" style="left:190px;top:420px">B</span>
    <div class="photo photo-police" role="img" aria-label="Male model in black police leather pants with blue stripe"></div>

    <div class="item" style="left:222px;top:422px;width:145px">
      <h3>C. Mens Athletic Briefs</h3> This athletic brief highlights your best assets while keeping you comfortable and secure all day. Made from a cotton-poly blend, these briefs stay in place thanks to the extra wide elastic waistband. <strong>Available</strong> in s, m, or L: small fits waists 26-30 inches, medium fits waists 30-34 inches, large fits waists 34-38 inches.
      <span class="sku">SG150 - $12.00</span>
    </div>
    <div class="item" style="left:374px;top:450px;width:172px">
      <h3>E. Blackout Body Suit</h3> Second skin from tip to toe! For HIM and HER: black body with hood, hands and feet. No openings but one zipper in the back. Slightly transparent, brilliant second skin fabric. Highly elastic and supple fabric. Made from 78 percent polyamide and 22 percent spandex. <strong>Available in XS, S, M, L, &amp; X-L</strong>
      <span class="sku">AA142 - $95.76</span>
    </div>

    <span class="tag" style="left:212px;top:625px">C</span>
    <div class="photo photo-briefs" role="img" aria-label="Black mens athletic briefs"></div>
    <span class="tag" style="left:386px;top:618px">D</span>
    <div class="photo photo-diaper" role="img" aria-label="Transparent latex diaper briefs"></div>
  </section>

</main>
</body>
</html>
```